Etiketten-Design für Getränkedose
Zielgruppe
Ich werde Getränke in Dosen 250 ml herstellen lassen, welches ich im Markt vertreiben möchte.
Aufgabenstellung
Das Pfandlogo und die EAN müssen an die Etiketten rangebracht werden, deshalb ist es wichtig, dass wenn Sie keine Möglichkeit haben die EAN ranzubringen, dass Platz im Design frei gehalten wird.
Im Anhang 1 finden Sie die Abmessungen von den Etiketten die an die Dosen rangebracht werden sollen!
Das Design muss innerhalb von diesen Abmessungen erstellt werden.
Es handelt sich hier nur um eine Druckvorlage!
Für so eine Druckvorlage muss auf den Etiketten Platz frei gehalten werden.
Ich benötige von Ihnen 3D Dosendesigns, sowie in meiner Skizze.
Wichtig: Es sollen auschließlich die Farben Weiß und Grün genutzt werden.
Meine Marke heißt ' Silver Plum' und es ist wichtig, dass die Farbe grün mit der Limette von meinem Logo passt.
Anhang 2&3= Mein Logo
Anhang 4= Eine Skizze von mir.
Ganz oben am Dosenrand soll das Wort Plum in Grün NICHT mit eingeführt werden.
Ganz unten soll bitte in Farbe Grau die Zahl: (2018) auf Römisch hinzugefügt werden und das Grau und die Schrift soll bitte mit meinem Logo passen:
MMXVIII
Wichtig: Es soll ein edles und modernes Design werden!
Ich freue mich auf Ihre kreativen Designs.
Als Vorgabe: Die Dose soll weiß sein und es sollen grüne Farben benutzt werden und es soll mit dem Logo farblich übereinstimmen.
Vielen Dank im Voraus

```html
<!DOCTYPE html>
<html lang="de">
<head>
<meta charset="utf-8">
<title>Silver Plum – Dosenetikett</title>
<link href="https://fonts.googleapis.com/css2?family=Raleway:wght@400&display=swap" rel="stylesheet">
<style>
  :root {
    --label-white: #ffffff;
    --page-bg: #f2f3f1;
    --leaf-deep: #1f8a2c;
    --leaf-mid: #4fae2f;
    --leaf-light: #a9d12e;
    --leaf-pale: #e4efb0;
    --text-grey: #6a6d6f;
    --year-grey: #8a8d8f;
    --band-line: #e3e5e2;
  }
  html, body {
    margin: 0;
    padding: 0;
    width: 805px;
    height: 1200px;
    overflow: hidden;
    background: var(--page-bg);
  }
  .label {
    position: relative;
    width: 805px;
    height: 1200px;
    background: var(--label-white);
    overflow: hidden;
  }
  .splash {
    position: absolute;
    left: 120px;
    width: 565px;
  }
  .splash--upper {
    top: 210px;
    height: 330px;
    background:
      radial-gradient(ellipse 55% 60% at 50% 75%, var(--leaf-deep) 0%, var(--leaf-mid) 35%, rgba(169,209,46,0.55) 62%, rgba(228,239,176,0) 82%);
  }
  .splash--lower {
    top: 650px;
    height: 300px;
    background:
      radial-gradient(ellipse 55% 60% at 50% 25%, var(--leaf-deep) 0%, var(--leaf-mid) 35%, rgba(169,209,46,0.55) 62%, rgba(228,239,176,0) 82%);
  }
  .name-band {
    position: absolute;
    top: 520px;
    left: 0;
    width: 805px;
    height: 150px;
    background: var(--label-white);
    border-top: 1px solid var(--band-line);
    border-bottom: 1px solid var(--band-line);
    display: flex;
    align-items: center;
    justify-content: center;
  }
  .brand-name {
    font-family: "Raleway", sans-serif;
    font-weight: 400;
    color: var(--text-grey);
    font-size: 40px;
    line-height: 1;
    letter-spacing: 0.18em;
    text-transform: uppercase;
    margin: 0;
    white-space: nowrap;
  }
  .year {
    position: absolute;
    top: 1065px;
    left: 0;
    width: 805px;
    text-align: center;
    font-family: "Raleway", sans-serif;
    font-weight: 400;
    font-size: 26px;
    letter-spacing: 0.28em;
    color: var(--year-grey);
    margin: 0;
  }
</style>
</head>
<body>
  <main class="label">
    <div class="splash splash--upper" role="img" aria-label="Grüne Blätter- und Farbspritzer-Illustration über dem Namensband"></div>
    <div class="splash splash--lower" role="img" aria-label="Grüne Blätter- und Farbspritzer-Illustration unter dem Namensband"></div>

    <section class="name-band">
      <h1 class="brand-name">Silver Plum</h1>
    </section>

    <p class="year">MMXVIII</p>
  </main>
</body>
</html>
```